CASH PAYMENT DISCOUNT NOTICE POSTED IN CASH REGISTER AREA

LOOKING TO MAKE A FLYER OR A POSTED NOTICE FOR CUSTOMERS PAYING FOR OVER-THE-COUNTER MERCHANDISE AND WHO PAY BY CASH METHOD TO GET A 4% CASH DISCOUNT.
PRESCRIPTIONS ARE EXCLUDED FROM THIS CASH DISCOUNT.

Target Market(s)

RETAIL CUSTOMERS

Industry/Entity Type

RETAIL PHARMACY

Colors
0054AA
0677BA
7BADD7
CADEEF
E8F1F8
EB3D1F
EC4F4E
F09395
F8D3D4
FCEDEE

Requirements
Must have
• LOGO COLORS
Nice to have
• EYE CATCHING

```html
<!DOCTYPE html>
<html lang="en">
<head>
<meta charset="utf-8">
<title>Customer Pricing Notice – Cash Discount</title>
<link rel="stylesheet" href="https://fonts.googleapis.com/css2?family=Outfit:wght@800&display=swap">
<style>
  :root {
    --brand-blue: #3f5ea8;
    --brand-red: #b53237;
    --paper: #ffffff;
    --ink-light: #ffffff;
  }
  html, body {
    margin: 0;
    padding: 0;
    overflow: hidden;
    background: var(--paper);
  }
  .notice {
    display: block;
    width: 1200px;
    height: 940px;
    background: var(--paper);
  }
  .notice text {
    font-family: "Outfit", "Poppins", sans-serif;
    font-weight: 800;
  }
  .headline { fill: var(--brand-blue); }
  .pill-bg, .ribbon-bg, .footer-band { fill: var(--brand-red); }
  .pill-text, .ribbon-text { fill: var(--ink-light); }
  .rate, .cash-word, .terms { fill: var(--brand-blue); }
  .brand-mark { fill: var(--brand-blue); }
  .brand-name { fill: var(--brand-red); }
</style>
</head>
<body>
<svg class="notice" viewBox="0 0 1200 940" xmlns="http://www.w3.org/2000/svg" role="img" aria-label="Customer pricing notice: this pharmacy has a 4% cash discount built into all pricing except on prescriptions">
  <defs>
    <linearGradient id="corner-top" x1="1" y1="0" x2="0" y2="1">
      <stop offset="0" stop-color="#b53237" stop-opacity="0.35"/>
      <stop offset="1" stop-color="#b53237" stop-opacity="0"/>
    </linearGradient>
    <linearGradient id="corner-bottom" x1="0" y1="1" x2="1" y2="0">
      <stop offset="0" stop-color="#b53237" stop-opacity="0.35"/>
      <stop offset="1" stop-color="#b53237" stop-opacity="0"/>
    </linearGradient>
  </defs>

  <!-- corner decoration areas -->
  <rect class="corner-accent" x="1030" y="0" width="170" height="140" fill="url(#corner-top)"
        role="img" aria-label="Red wavy ribbon ornament in the top-right corner"/>
  <rect class="corner-accent" x="0" y="805" width="90" height="107" fill="url(#corner-bottom)"
        role="img" aria-label="Red looping ribbon ornament in the bottom-left corner"/>
  <rect class="footer-band" x="68" y="912" width="1132" height="28"/>

  <!-- heading -->
  <text class="headline" x="600" y="122" font-size="64" text-anchor="middle" textLength="600" lengthAdjust="spacingAndGlyphs">CUSTOMER PRICING</text>
  <text class="headline" x="600" y="186" font-size="64" text-anchor="middle" textLength="222" lengthAdjust="spacingAndGlyphs">NOTICE</text>

  <!-- intro pill -->
  <rect class="pill-bg" x="276" y="229" width="642" height="62" rx="20"/>
  <text class="pill-text" x="597" y="280" font-size="56" text-anchor="middle" textLength="610" lengthAdjust="spacingAndGlyphs">THIS PHARMACY HAS A</text>

  <!-- discount rate -->
  <text class="rate" x="128" y="536" font-size="308" textLength="489" lengthAdjust="spacingAndGlyphs">4%</text>
  <text class="cash-word" x="710" y="405" font-size="122" textLength="298" lengthAdjust="spacingAndGlyphs">CASH</text>

  <g class="discount-ribbon" transform="translate(647 420)">
    <path class="ribbon-bg"
          d="M0,0 L424,0 L410,14 L424,27 L405,45 L424,69 L410,95 L424,120 L0,120 L13,105 L0,92 L19,75 L0,51 L13,24 Z"/>
    <text class="ribbon-text" x="27" y="84" font-size="68" textLength="369" lengthAdjust="spacingAndGlyphs">DISCOUNT</text>
  </g>

  <!-- terms -->
  <text class="terms" x="172" y="617" font-size="58" textLength="855" lengthAdjust="spacingAndGlyphs">BUILT INTO ALL PRICING EXCEPT</text>
  <text class="terms" x="336" y="690" font-size="58" textLength="526" lengthAdjust="spacingAndGlyphs">ON PRESCRIPTIONS</text>

  <!-- brand sign-off -->
  <g class="brand">
    <rect class="brand-mark" x="380" y="790" width="40" height="40"/>
    <text class="brand-name" x="436" y="828" font-size="50" textLength="400" lengthAdjust="spacingAndGlyphs">Maple Row Pharmacy</text>
  </g>
</svg>
</body>
</html>
```